NZ First of it's kind solutions directory and marketplace for busy Mums needs a business card design

We need a business card design for our new nationwide business in NZ (long term plans to go global). We provide solutions to the everyday challenges that busy Mums face by connecting them with quality communities and suppliers of carefully selected, relevant products and services. We sell direct via our online marketplace. The final design should communicate our values of inclusivity, quality and smart solutions. Colours should incorporate our logo colour palette of #477077 and #6ba8b2. Our website is at https://www.brightnestly.com

Target Market(s)

busy Mums, Age 28 – 50, female, income over $100K, location main centres NZ primarily but NZ wide. Is likely juggling work or career with a young family. Probably had hobbies which have fallen by the wayside.
-Wants to succeed in her chosen career without compromising on family life
-to successfully juggle her career without feeling like she is compromising her children
- Is time poor, something always has to give and it’s generally her health (she’ll stay up late, get stressed)
- probably ex corporate or professional career. Has discretional income

Industry/Entity Type

Business

Contact Information for Business Card

Jodie Farnsworth, Founder, BrightNestly.com (Strapline Browse; Pick; Sorted), 48 Kowhai Terrace, Hillsborough, Auckland 1058, New Zealand. Mob: 021 437 518 Ph: +64 (0)9 584 7163

Font styles to use
Other font styles liked:
• Raleway, and/or Architects Daughter

Colors
00a990
33b8a4
86cfc6
cfeae6

Requirements
Must have
• the above details, streamline. the logo and colours associated with those logos
Should not have
• foil or metallic colours

```html
<!DOCTYPE html>
<html lang="en">
<head>
<meta charset="utf-8">
<title>BrightNestly Business Card</title>
<link rel="stylesheet" href="https://fonts.googleapis.com/css2?family=Architects+Daughter&family=Raleway:wght@400;600;800&display=swap">
<style>
  :root {
    --backdrop: #2f7471;
    --card: #d3ece6;
    --card-watermark: #c4e3dc;
    --teal-dark: #477077;
    --teal-mid: #3f7c78;
    --teal-light: #4fb7a5;
    --text-body: #3d6664;
  }
  * { box-sizing: border-box; margin: 0; padding: 0; }
  html, body {
    width: 1200px;
    height: 1000px;
    overflow: hidden;
    background: var(--backdrop);
  }
  .canvas {
    width: 1200px;
    height: 1000px;
    display: flex;
    flex-direction: column;
    align-items: center;
    justify-content: center;
    gap: 60px;
  }
  .card {
    position: relative;
    width: 720px;
    height: 400px;
    background: var(--card);
    overflow: hidden;
    border-radius: 4px;
    box-shadow: 0 10px 30px rgba(0, 0, 0, 0.22);
  }
  .card-watermark {
    position: absolute;
    left: -40px;
    top: -70px;
    font-family: "Raleway", sans-serif;
    font-weight: 800;
    font-size: 300px;
    line-height: 1;
    letter-spacing: -6px;
    color: var(--card-watermark);
    white-space: nowrap;
    transform: rotate(-8deg);
    pointer-events: none;
    user-select: none;
  }
  .card-content { position: relative; height: 100%; }

  /* Brand side */
  .brand {
    position: absolute;
    left: 110px;
    top: 145px;
    display: flex;
    align-items: center;
    gap: 26px;
  }
  .brand-dot {
    width: 96px;
    height: 96px;
    border-radius: 50%;
    background: var(--teal-dark);
    flex: none;
  }
  .brand-name {
    font-family: "Raleway", sans-serif;
    font-weight: 800;
    font-size: 62px;
    letter-spacing: -1px;
    line-height: 1;
    color: var(--teal-dark);
  }
  .brand-tagline {
    margin-top: 8px;
    margin-left: 4px;
    font-family: "Architects Daughter", cursive;
    font-size: 24px;
    color: var(--text-body);
  }

  /* Contact side */
  .contact {
    display: flex;
    flex-direction: column;
    align-items: center;
    text-align: center;
    padding-top: 34px;
  }
  .contact-dot {
    width: 34px;
    height: 34px;
    border-radius: 50%;
    background: var(--teal-dark);
  }
  .contact-name {
    margin-top: 12px;
    font-family: "Architects Daughter", cursive;
    font-size: 46px;
    letter-spacing: 2px;
    line-height: 1.05;
    color: var(--teal-mid);
    text-transform: uppercase;
  }
  .contact-role {
    font-family: "Architects Daughter", cursive;
    font-size: 26px;
    letter-spacing: 1px;
    color: var(--teal-light);
    text-transform: uppercase;
  }
  .contact-site {
    margin-top: 26px;
    font-family: "Raleway", sans-serif;
    font-weight: 800;
    font-size: 25px;
    color: var(--text-body);
  }
  .contact-strapline {
    font-family: "Raleway", sans-serif;
    font-weight: 400;
    font-size: 19px;
    color: var(--teal-light);
  }
  .contact-address {
    margin-top: 40px;
    font-family: "Raleway", sans-serif;
    font-weight: 600;
    font-size: 19px;
    color: var(--teal-light);
  }
  .contact-phones {
    margin-top: 8px;
    font-family: "Raleway", sans-serif;
    font-weight: 600;
    font-size: 19px;
    color: var(--teal-light);
    display: flex;
    gap: 40px;
  }
  .contact-phones b { color: var(--text-body); font-weight: 800; }
</style>
</head>
<body>
<main class="canvas">
  <section class="card card-front" aria-label="Business card brand side">
    <div class="card-watermark" aria-hidden="true">Nestly</div>
    <div class="card-content">
      <div class="brand">
        <span class="brand-dot" aria-hidden="true"></span>
        <div>
          <div class="brand-name">BrightNestly</div>
          <div class="brand-tagline">Solutions for Busy Mums.</div>
        </div>
      </div>
    </div>
  </section>

  <section class="card card-back" aria-label="Business card contact side">
    <div class="card-watermark" aria-hidden="true">Nestly</div>
    <div class="card-content contact">
      <span class="contact-dot" aria-hidden="true"></span>
      <h1 class="contact-name">Jodie Farnsworth</h1>
      <p class="contact-role">Founder</p>
      <p class="contact-site">BrightNestly.com</p>
      <p class="contact-strapline">Browse. Pick. Sorted</p>
      <p class="contact-address">48 Kowhai Terrace, Hillsborough, Auckland 1058, New Zealand</p>
      <p class="contact-phones">
        <span><b>M:</b> 021 437 518</span>
        <span><b>P:</b> +64 (0)9 584 7163</span>
      </p>
    </div>
  </section>
</main>
</body>
</html>
```